DMVN Website

Hi we require a website with similar attributes and design to this http://style5.tarnbridgepages.com but obviously with all our information and images etc... also attached are our logos please do the design with the yellow logo not the red.

```html
<!DOCTYPE html>
<html lang="en">
<head>
<meta charset="utf-8">
<title>DMVN – Dunmoor Collision Repair Centre</title>
<link rel="stylesheet" href="https://fonts.googleapis.com/css2?family=Oswald:wght@300;400;500;600&family=Open+Sans:wght@400;600;700&display=swap">
<style>
:root{
  --yellow:#f2c40f;
  --black:#050505;
  --dark:#1b1b1b;
  --panel:#262626;
  --teal:#6e9a92;
  --teal-deep:#2d5a52;
  --white:#ffffff;
  --muted:#cfcfcf;
  --nav:#2c2c2c;
  --footer:#222222;
}
*{margin:0;padding:0;box-sizing:border-box}
html,body{width:1200px;height:2956px;overflow:hidden;background:var(--black)}
body{font-family:"Open Sans",Arial,sans-serif;color:var(--white);position:relative}
.head,.hero,.about,.services,.gallery,.reviews,.footer{position:absolute;left:0;width:1200px}
h1,h2,h3,h4,.nav a,.btn,.brand{font-family:"Oswald","Arial Narrow",sans-serif;font-weight:500;text-transform:uppercase}

/* header */
.head{top:0;height:100px;z-index:2}
.brand{position:absolute;left:88px;top:30px;display:flex;align-items:center;gap:14px;color:var(--yellow);font-size:64px;font-weight:600;letter-spacing:4px;line-height:1}
.brand-mark{width:22px;height:22px;background:var(--yellow)}
.phone{position:absolute;right:70px;top:8px;display:flex;align-items:center;gap:8px;font-size:15px;font-weight:600}
.navbar{position:absolute;left:342px;top:38px;right:0;height:56px;background:var(--nav);display:flex;align-items:center}
.navbar::before{content:"";position:absolute;left:2px;top:0;width:6px;height:56px;background:var(--yellow);transform:skewX(-18deg)}
.nav{display:flex;gap:22px;margin-left:42px}
.nav a{color:var(--white);text-decoration:none;font-size:14.5px;font-weight:400}

/* hero */
.hero{top:0;height:650px;background:radial-gradient(ellipse at 55% 60%,#3a3a3a 0%,#151515 55%,#050505 100%)}
.hero-car{position:absolute;left:240px;top:260px;width:740px;height:250px;border-radius:120px 200px 40px 40px;background:linear-gradient(180deg,#6a6a6a 0%,#3b3b3b 55%,#1a1a1a 100%)}
.hero-kicker{position:absolute;left:154px;top:216px;font-family:"Oswald",sans-serif;font-weight:300;font-size:26px;text-transform:uppercase;display:flex;align-items:center;gap:12px}
.hero-kicker i{width:3px;height:24px;background:var(--yellow)}
.hero-title{position:absolute;left:154px;top:252px;font-size:45px;font-weight:500}
.dots{position:absolute;left:574px;top:584px;display:flex;gap:7px}
.dots span{width:11px;height:11px;border-radius:50%;background:#9a9a9a}
.dots .on{background:var(--yellow)}

/* about */
.about{top:650px;height:462px;background:var(--black)}
.feature{position:absolute;left:86px;width:414px;height:104px;background:var(--panel);display:flex;overflow:hidden}
.feature.active{background:var(--teal)}
.feature-icon{width:150px;height:104px;background:#171717;clip-path:polygon(0 0,100% 0,74% 100%,0 100%);display:flex;align-items:center;padding-left:26px}
.feature.active .feature-icon{background:#1d1d1d}
.feature-text{padding:20px 0 0 4px}
.feature h4{font-size:14.5px;font-weight:500}
.feature p{font-size:12.5px;color:#e0e0e0;margin-top:8px;line-height:1.55;width:250px}
.about-copy{position:absolute;left:538px;top:42px;width:580px}
.about-copy .eyebrow{font-family:"Oswald",sans-serif;font-weight:300;font-size:24px}
.about-copy h2{font-size:30px;margin-top:2px}
.about-copy p{font-size:12.6px;line-height:1.75;margin-top:18px;color:#eaeaea}
.btn{display:inline-block;background:var(--yellow);color:#111;font-size:14.5px;font-weight:400;padding:9px 22px;border-radius:22px}
.about-copy .btn{margin-top:28px}

/* services */
.services{top:1112px;height:600px;background:var(--dark)}
.sec-title{position:absolute;left:0;width:1200px;text-align:center;top:38px;font-size:31px}
.bar{display:flex;gap:8px}
.bar i{height:4px;background:var(--yellow);display:block}
.services .bar{position:absolute;left:549px;top:92px}
.svc{position:absolute;width:350px}
.svc h4{font-size:17px;font-weight:400}
.svc p{font-size:12.4px;line-height:1.55;color:#d0d0d0;margin-top:10px;width:240px}
.svc-icon{position:absolute;width:86px;height:86px;border-radius:50%;border:2px dashed var(--yellow);display:flex;align-items:center;justify-content:center}
.dotline{position:absolute;border-top:2px dotted #777;height:0}
.emblem{position:absolute;left:445px;top:138px;width:310px;height:310px}
.emblem-name{position:absolute;left:0;top:130px;width:310px;text-align:center;font-family:"Oswald",sans-serif;font-weight:600;font-size:44px;color:var(--yellow);letter-spacing:3px}

/* gallery */
.gallery{top:1712px;height:738px;background:var(--black)}
.gallery h2{position:absolute;left:86px;top:64px;font-size:31px}
.gallery .bar{position:absolute;left:86px;top:116px}
.gallery .lead{position:absolute;left:86px;top:138px;width:1030px;font-size:12.6px;line-height:1.75;color:#e6e6e6}
.photo{position:absolute;overflow:hidden}
.photo .tag{position:absolute;top:8px;font-family:"Oswald",sans-serif;font-style:italic;font-weight:300;font-size:17px;color:#111}
.photo .tag.light{color:#f2f2f2}
.gallery .btn{position:absolute;left:498px;top:626px}

/* reviews */
.reviews{top:2450px;height:454px;background:linear-gradient(180deg,#3a6a61 0%,var(--teal-deep) 100%)}
.reviews h2{position:absolute;left:86px;top:36px;font-size:31px}
.reviews .bar{position:absolute;left:86px;top:88px}
.card{position:absolute;top:112px;width:326px;height:222px;border:1px solid #8cc1b7;text-align:center}
.card .q{font-family:Georgia,serif;font-size:54px;color:#fff;line-height:1;margin-top:14px}
.card p{font-size:12.5px;line-height:1.7;padding:6px 22px 0}
.avatar{position:absolute;left:129px;top:190px;width:68px;height:68px;border-radius:50%;border:3px solid #fff;background:linear-gradient(180deg,#d8b9a0,#9a7a63)}
.card .name{position:absolute;left:0;top:272px;width:326px;font-size:13px;font-weight:700}
.chev{position:absolute;top:203px}

/* footer */
.footer{top:2904px;height:52px;background:var(--footer);display:flex;align-items:center;justify-content:space-between;padding:0 86px}
.social{display:flex;gap:14px}
.social span{width:12px;height:12px;border-radius:50%;background:#fff}
.copy{font-size:12.5px;color:#bdbdbd}
</style>
</head>
<body>

<section class="hero">
  <div class="hero-car" role="img" aria-label="Photo of a dark grey sports coupe in a dim studio"></div>
  <div class="hero-kicker"><i></i>Highly Trained<i></i></div>
  <h1 class="hero-title">Auto Body Technicians</h1>
  <div class="dots"><span></span><span class="on"></span><span></span></div>
</section>

<header class="head">
  <div class="brand"><span class="brand-mark"></span>DMVN</div>
  <div class="phone">
    <svg width="16" height="16" viewBox="0 0 24 24"><path fill="#f2c40f" d="M6.6 10.8a15.1 15.1 0 0 0 6.6 6.6l2.2-2.2c.3-.3.7-.4 1-.2 1.1.4 2.3.6 3.6.6.6 0 1 .4 1 1V20c0 .6-.4 1-1 1A17 17 0 0 1 3 4c0-.6.4-1 1-1h3.5c.6 0 1 .4 1 1 0 1.3.2 2.5.6 3.6.1.3 0 .7-.2 1z"/></svg>
    (555) 014-2290
  </div>
  <nav class="navbar">
    <div class="nav">
      <a href="#">Home</a><a href="#">Online Estimate Request</a><a href="#">Services</a><a href="#">Repair Status Update</a><a href="#">Contact Us</a><a href="#">Before and After</a><a href="#">Testimonials</a>
    </div>
  </nav>
</header>

<section class="about">
  <div class="feature active" style="top:48px">
    <div class="feature-icon"><svg width="62" height="56" viewBox="0 0 62 56" fill="none" stroke="#fff" stroke-width="4"><path d="M3 22 31 4l28 18v32H3z"/><rect x="14" y="30" width="34" height="18" rx="3"/></svg></div>
    <div class="feature-text"><h4>Modern Workshop</h4><p>Sed ut perspiciatis unde omnis iste natus error sit voluptatem accusantium</p></div>
  </div>
  <div class="feature" style="top:168px">
    <div class="feature-icon"><svg width="56" height="56" viewBox="0 0 56 56" fill="#fff"><path d="M8 30a20 20 0 0 1 40 0h4v6H4v-6z"/><rect x="12" y="40" width="32" height="14" rx="3"/></svg></div>
    <div class="feature-text"><h4>Talented Workers</h4><p>Sed ut perspiciatis unde omnis iste natus error sit voluptatem accusantium</p></div>
  </div>
  <div class="feature" style="top:288px">
    <div class="feature-icon"><svg width="58" height="58" viewBox="0 0 58 58" fill="none" stroke="#fff" stroke-width="5"><circle cx="29" cy="29" r="24" stroke-dasharray="8 4"/><circle cx="29" cy="29" r="10"/></svg></div>
    <div class="feature-text"><h4>Leading Auto Specialist</h4><p>Sed ut perspiciatis unde omnis iste natus error sit voluptatem accusantium</p></div>
  </div>
  <div class="about-copy">
    <div class="eyebrow">ABOUT</div>
    <h2>Dunmoor Collision Repair Centre</h2>
    <p>We're excited to launch our new website! Please feel free to leave comments and suggestions. We are continually striving to improve our service and we welcome your input. At Style 5, we make customer service a priority. Our people are highly trained and are dedicated to the commitment of quality, workmanship and service that our business was in fact, founded on.</p>
    <p>Our technicians have several years of experience behind them. We're proud to serve the auto body repair needs of the Dallas area. When the safety of your family is on the line, why settle for second best.</p>
    <span class="btn">Online Estimate Request</span>
  </div>
</section>

<section class="services">
  <h2 class="sec-title">Our Services</h2>
  <div class="bar" style="left:549px"><i style="width:40px"></i><i style="width:36px"></i></div>

  <svg class="emblem" viewBox="0 0 310 310">
    <circle cx="155" cy="155" r="150" fill="none" stroke="#d8d8d8" stroke-width="3" stroke-dasharray="22 12"/>
    <circle cx="155" cy="155" r="126" fill="#050505"/>
  </svg>
  <div class="emblem-name" style="left:445px;top:268px;width:310px">DMVN</div>

  <!-- left column -->
  <div class="svc-icon" style="left:86px;top:104px"><svg width="46" height="30" viewBox="0 0 46 30" fill="#fff"><path d="M4 14l8-10h20l10 10v10H4z"/><circle cx="13" cy="25" r="5"/><circle cx="34" cy="25" r="5"/></svg></div>
  <div class="svc" style="left:192px;top:160px"><h4>Auto Body Repair</h4><p>Sed ut perspiciatis unde omnis iste nat us error sit voluptatem</p></div>

  <div class="svc-icon" style="left:86px;top:256px"><svg width="40" height="40" viewBox="0 0 40 40" stroke="#fff" stroke-width="5" stroke-linecap="round"><path d="M6 6l28 28M34 6 6 34"/></svg></div>
  <div class="svc" style="left:192px;top:316px"><h4>Paintless Dent Repair</h4><p>Sed ut perspiciatis unde omnis iste nat us error sit voluptatem</p></div>
  <div class="dotline" style="left:182px;top:299px;width:252px"></div>

  <div class="svc-icon" style="left:86px;top:408px"><svg width="46" height="32" viewBox="0 0 46 32" fill="#fff"><path d="M2 20V10h14l6 10h22v6H2z"/><path d="M28 18 40 4" stroke="#fff" stroke-width="3"/><circle cx="11" cy="27" r="5"/><circle cx="35" cy="27" r="5"/></svg></div>
  <div class="svc" style="left:192px;top:466px"><h4>Towing</h4><p>Sed ut perspiciatis unde omnis iste nat us error sit voluptatem</p></div>
  <div class="dotline" style="left:182px;top:451px;width:290px"></div>
  <div class="dotline" style="left:182px;top:147px;width:290px"></div>

  <!-- right column -->
  <div class="svc-icon" style="left:1028px;top:104px"><svg width="42" height="42" viewBox="0 0 42 42" fill="none" stroke="#fff" stroke-width="4"><circle cx="21" cy="21" r="17"/><circle cx="21" cy="21" r="5"/><path d="M21 4v12M4 21h12M26 21h12"/></svg></div>
  <div class="svc" style="left:798px;top:160px"><h4>Auto Body Refinishing</h4><p>Sed ut perspiciatis unde omnis iste nat us error sit voluptatem</p></div>
  <div class="dotline" style="left:728px;top:147px;width:290px"></div>

  <div class="svc-icon" style="left:1028px;top:256px"><svg width="44" height="30" viewBox="0 0 44 30" fill="none" stroke="#fff" stroke-width="4"><path d="M4 4q18-4 36 0l-4 22q-14 2-28 0z"/></svg></div>
  <div class="svc" style="left:798px;top:316px"><h4>Auto Glass Repair and<br>Replacement</h4><p>Sed ut perspiciatis unde omnis iste nat us error sit voluptatem</p></div>
  <div class="dotline" style="left:766px;top:299px;width:252px"></div>

  <div class="svc-icon" style="left:1028px;top:408px"><svg width="42" height="36" viewBox="0 0 42 36" fill="none" stroke="#fff" stroke-width="3"><circle cx="5" cy="6" r="3"/><circle cx="5" cy="18" r="3"/><circle cx="5" cy="30" r="3"/><path d="M14 6h26M14 18h26M14 30h26"/></svg></div>
  <div class="svc" style="left:798px;top:466px"><h4>Automotive Detailing</h4><p>Sed ut perspiciatis unde omnis iste nat us error sit voluptatem</p></div>
  <div class="dotline" style="left:728px;top:451px;width:290px"></div>
</section>

<section class="gallery">
  <h2>Auto Body Repair Before &amp; After Pictures</h2>
  <div class="bar"><i style="width:64px"></i><i style="width:22px"></i></div>
  <p class="lead">Sed ut perspiciatis unde omnis iste natus error sit voluptatem accusantium doloremque laudantium, totam rem aperiam, eaque ipsa quae ab illo inventore veritatis et quasi architecto beatae vitae dicta sunt explicabo. Nemo enim ipsam voluptatem quia voluptas sit aspernatur aut odit aut fugit</p>

  <div class="photo" style="left:86px;top:213px;width:412px;height:228px;background:linear-gradient(90deg,#b9a3b6 0%,#e8e8ea 45%,#9a9a9f 100%)" role="img" aria-label="Before and after photo of a repaired crossover SUV">
    <span class="tag" style="left:16px">After</span><span class="tag" style="left:170px">Before</span>
  </div>
  <div class="photo" style="left:524px;top:213px;width:592px;height:228px;background:linear-gradient(90deg,#6f6f6f 0%,#c9c9c9 48%,#c7a071 52%,#6e5a42 100%)" role="img" aria-label="Before and after photo of a restored vintage car in a field">
    <span class="tag" style="left:12px">Before</span><span class="tag light" style="left:312px">After</span>
  </div>

  <div class="photo" style="left:86px;top:465px;width:326px;height:121px;background:linear-gradient(90deg,#4e8a7a,#a0774a 50%,#5c6b6a)" role="img" aria-label="Close-up of an old car headlight and grille"></div>
  <div class="photo" style="left:437px;top:465px;width:326px;height:121px;background:linear-gradient(90deg,#a8906a,#6b5a46 45%,#b03226 70%,#c9c9c9)" role="img" aria-label="Classic cars parked outdoors with chrome details"></div>
  <div class="photo" style="left:788px;top:465px;width:328px;height:121px;background:linear-gradient(90deg,#7fa8a4,#d2d2d2 45%,#3f8a86 75%,#c44d3a)" role="img" aria-label="Chrome headlight and tail fin of a vintage car"></div>

  <span class="btn">Online Estimate Request</span>
</section>

<section class="reviews">
  <h2>What Peolpe Are Saying</h2>
  <div class="bar"><i style="width:64px"></i><i style="width:22px"></i></div>

  <svg class="chev" style="left:40px" width="14" height="40" viewBox="0 0 14 40" fill="none" stroke="#cfe3df" stroke-width="2"><path d="M12 2 2 20l10 18"/></svg>
  <svg class="chev" style="left:1146px" width="14" height="40" viewBox="0 0 14 40" fill="none" stroke="#cfe3df" stroke-width="2"><path d="M2 2l10 18L2 38"/></svg>

  <div class="card" style="left:86px">
    <div class="q">&#8220;</div>
    <p>Sed ut perspiciatis unde omnis iste natus error sit voluptatem accusantium doloremque laudantium, totam rem aperiam, eaque ipsa quae ab illo inventore veritatis et quasi architecto beatae vitae</p>
    <div class="avatar" role="img" aria-label="Customer portrait"></div>
    <div class="name">Dan Harlow</div>
  </div>
  <div class="card" style="left:437px">
    <div class="q">&#8220;</div>
    <p>Sed ut perspiciatis unde omnis iste natus error sit voluptatem accusantium doloremque laudantium, totam rem aperiam, eaque ipsa quae ab illo inventore veritatis et quasi architecto beatae vitae</p>
    <div class="avatar" role="img" aria-label="Customer portrait"></div>
    <div class="name">Dan Harlow</div>
  </div>
  <div class="card" style="left:790px">
    <div class="q">&#8220;</div>
    <p>Sed ut perspiciatis unde omnis iste natus error sit voluptatem accusantium doloremque laudantium, totam rem aperiam, eaque ipsa quae ab illo inventore veritatis et quasi architecto beatae vitae</p>
    <div class="avatar" role="img" aria-label="Customer portrait"></div>
    <div class="name">Dan Harlow</div>
  </div>
</section>

<footer class="footer">
  <div class="social" aria-label="Social links"><span></span><span></span><span></span></div>
  <div class="copy">© 2018 All Rights Reserved. Terms of Use and Privacy Policy</div>
</footer>

</body>
</html>
```